Refresh of Business Card Design

Want to refresh the business card design with the new logo while adhering to style guide as attached. Would like to match feel of website www.durmackvinex.com

```html
<!DOCTYPE html>
<html lang="en">
<head>
<meta charset="utf-8">
<title>Durmack Vinex – Business Card</title>
<link rel="stylesheet" href="https://fonts.googleapis.com/css2?family=Montserrat:wght@300;400;800&family=Work+Sans:wght@400;500;700&display=swap">
<style>
  :root{
    --page:#d9d9d9;
    --card-white:#f4f4f4;
    --card-black:#070707;
    --ink:#111111;
    --accent:#e0203f;
    --paper-text:#ffffff;
    --muted:#2a2a2a;
  }
  *{margin:0;padding:0;box-sizing:border-box}
  html,body{width:1200px;height:1200px;overflow:hidden}
  body{
    background:var(--page);
    display:flex;flex-direction:column;align-items:center;justify-content:center;gap:90px;
    font-family:"Work Sans",sans-serif;
  }
  .card{
    width:700px;height:400px;position:relative;
    box-shadow:0 10px 30px rgba(0,0,0,.18);
  }
  /* front */
  .card--front{background:var(--card-white);display:flex;flex-direction:column;align-items:center;justify-content:center}
  .brand{display:flex;align-items:center;gap:16px}
  .brand__dot{width:44px;height:44px;border-radius:50%;background:var(--accent)}
  .brand__name{
    font-family:"Work Sans",sans-serif;font-weight:700;font-size:40px;
    color:var(--ink);letter-spacing:1px;text-transform:uppercase;
  }
  .person{margin-top:46px;text-align:center;color:var(--ink)}
  .person__name{font-weight:700;font-size:34px;line-height:1.1}
  .person__role{font-weight:400;font-size:30px;color:var(--muted);line-height:1.2}
  /* back */
  .card--back{background:var(--card-black);color:var(--paper-text);padding:48px 52px}
  .wordmark__top{
    font-family:"Montserrat",sans-serif;font-weight:800;font-size:98px;line-height:.9;letter-spacing:1px;
  }
  .wordmark__bottom{
    font-family:"Montserrat",sans-serif;font-weight:300;font-size:108px;line-height:.95;color:var(--accent);
  }
  .wordmark__web{font-family:"Montserrat",sans-serif;font-weight:400;font-size:27px;margin-top:6px;letter-spacing:.5px}
  .contact{position:absolute;right:40px;bottom:34px;font-size:15.5px;line-height:1.3}
  .contact__cell{color:var(--accent);font-weight:700;font-size:20px}
  .contact__email{font-weight:500}
</style>
</head>
<body>
  <section class="card card--front">
    <div class="brand">
      <span class="brand__dot"></span>
      <span class="brand__name">Durmack Vinex</span>
    </div>
    <div class="person">
      <p class="person__name">Corwin Baylis</p>
      <p class="person__role">Sales</p>
    </div>
  </section>

  <section class="card card--back">
    <div class="wordmark">
      <p class="wordmark__top">DURMACK</p>
      <p class="wordmark__bottom">vinex</p>
      <p class="wordmark__web">www.durmackvinex.com</p>
    </div>
    <div class="contact">
      <p class="contact__cell">Cell : 555.214.3097</p>
      <p>P.O. Box 48230 Odell, Tx 79502</p>
      <p>72 Harlan Ridge Dr Keller, Texas 79230</p>
      <p class="contact__email">cbaylis@durmackvinex.com</p>
    </div>
  </section>
</body>
</html>
```